Graphic Design for a block-note A4 size

We need a graphic design for a simple block-note A4 size. The product consists of 50 sheets in VERTICAL A4 (21x29,7cm) size, simply glued on top, without cover. We would like to have proposals with double application: one for home users without a logo and one for professionals with an area "put your logo here".
The graphics should be simple and attractive, elegant and pleasant to keep on your desk.
The block-notes may have standard squares (5 or 10 mm) or stripes (10 mm spaced) on the background to make the writing easy.
Feel free to use your creativity, the only limit is the CMYK color space.

We will upload some block-note simple templates and 3D sample images to help you.

• The graphics should be simple and attractive, elegant and pleasant to keep on your desk.

• The block-notes may have standard squares (5 or 10 mm) or stripes (10 mm spaced) on the background to make the writing easy.

```html
<!DOCTYPE html>
<html lang="en">
<head>
<meta charset="utf-8">
<title>A4 Block-Note Designs</title>
<link href="https://fonts.googleapis.com/css2?family=Open+Sans:wght@600&display=swap" rel="stylesheet">
<style>
  :root {
    --canvas-bg: #f2f2f0;
    --sheet-bg: #ffffff;
    --grid-line: #c9ccd0;
    --blue-band: #bfe1f5;
    --blue-text: #4a9fd8;
    --green-band: #dcebc4;
    --green-text: #a7c77a;
    --oval-white: rgba(255, 255, 255, 0.9);
    --sheet-shadow: rgba(0, 0, 0, 0.18);
  }
  * { margin: 0; padding: 0; box-sizing: border-box; }
  html, body {
    width: 1200px;
    height: 1007px;
    overflow: hidden;
    background: var(--canvas-bg);
  }
  .canvas {
    position: relative;
    width: 1200px;
    height: 1007px;
    display: flex;
    justify-content: center;
    align-items: center;
    gap: 70px;
  }
  .note-sheet {
    position: relative;
    width: 500px;
    height: 707px;
    background-color: var(--sheet-bg);
    background-image:
      linear-gradient(to right, var(--grid-line) 1px, transparent 1px),
      linear-gradient(to bottom, var(--grid-line) 1px, transparent 1px);
    background-size: 23.8px 23.8px;
    background-position: 6px 6px;
    box-shadow: 0 4px 14px var(--sheet-shadow);
    overflow: hidden;
  }
  .logo-band {
    position: absolute;
    left: 0;
    bottom: 0;
    width: 500px;
    height: 240px;
  }
  .logo-placeholder {
    position: absolute;
    font-family: "Open Sans", Arial, sans-serif;
    font-weight: 600;
    font-size: 26px;
    letter-spacing: -0.5px;
  }
  .note-sheet--blue .logo-placeholder {
    color: var(--blue-text);
    left: 150px;
    bottom: 78px;
  }
  .note-sheet--green .logo-placeholder {
    color: var(--green-text);
    left: 190px;
    bottom: 88px;
  }
</style>
</head>
<body>
  <main class="canvas">
    <section class="note-sheet note-sheet--blue" aria-label="Block-note with blue logo area">
      <svg class="logo-band" viewBox="0 0 500 240" aria-hidden="true">
        <ellipse cx="300" cy="150" rx="290" ry="105" transform="rotate(-18 300 150)" fill="var(--blue-band)"/>
        <ellipse cx="250" cy="172" rx="245" ry="82" transform="rotate(-14 250 172)" fill="var(--oval-white)"/>
      </svg>
      <span class="logo-placeholder">LOGOHERE</span>
    </section>

    <section class="note-sheet note-sheet--green" aria-label="Block-note with green logo area">
      <svg class="logo-band" viewBox="0 0 500 240" aria-hidden="true">
        <ellipse cx="290" cy="150" rx="300" ry="95" transform="rotate(-8 290 150)" fill="var(--green-band)"/>
        <ellipse cx="250" cy="168" rx="250" ry="78" transform="rotate(-5 250 168)" fill="var(--oval-white)"/>
      </svg>
      <span class="logo-placeholder">LOGOHERE</span>
    </section>
  </main>
</body>
</html>
```